Logo & Visitenkarte für Elterncoaching, Einzel,- Paar- und Familientherapie
Tolle eigene kreative Umsetzung, super schnell in der Kommunikation und im Umgang mit Input. Eine große Unterstützung und sehr professionell. Die Zusammenarbeit hat viel Spaß gemacht und ich kann Nachtfalke empfehlen!
Zielgruppe
Tätigkeit: Elterncoaching, Einzel,- Paar- und Familientherapie
Zielgruppe: Eltern kleiner Kinder, Paare, Einzelne Personen die nicht mehr weiter wissen oder einfach eine neue Idee / Perspektiven benötigen
Aufgabenstellung
Auf die Visitenkarte soll ein Logo bzw. eine Grafik dargestellt werden, welche ebenfalls auf der Website und dem Flyer genutzt werden soll wird es hier als Logo bezeichnet.
Die Grafik soll ein Labyrinth und eine Person in einer scheinbar aussichtsloser Lage darstellen mit der Frage „ANKER gefällig?“ (siehe Idee im Datenanhang).
Die Figur soll oben links stehen und in Richtung Labyrinth blicken (hier zu beachten dass es bei einem eventuellen Druck von Visitenkarten mit abgerundeten Kanten nicht angeschnitten wird).
WICHTIG: bei der Figur soll nicht zu erkennen sein ob es sich um eine weibliche oder männliche Person handelt, es soll sowohl für Einzelpersonen als auch für Paare oder Familien ansprechend wirken.

```html
<!DOCTYPE html>
<html lang="de">
<head>
<meta charset="utf-8">
<title>Praxis Ankerplatz – Visitenkarte</title>
<link href="https://fonts.googleapis.com/css2?family=Barlow+Semi+Condensed:wght@300;400;600;700&display=swap" rel="stylesheet">
<style>
  :root {
    --stage: #3a3a3a;
    --ink: #111111;
    --paper: #ffffff;
    --card-black: #0d0d0d;
  }
  * { box-sizing: border-box; margin: 0; padding: 0; }
  html, body {
    width: 1200px; height: 895px; overflow: hidden;
    background: var(--stage);
    font-family: "Barlow Semi Condensed", "Arial Narrow", sans-serif;
  }
  .stage {
    width: 1200px; height: 895px;
    display: flex; align-items: center; justify-content: center; gap: 90px;
  }
  .card {
    width: 400px; height: 620px;
    border-radius: 4px;
    box-shadow: 0 18px 40px rgba(0,0,0,.35);
  }

  /* Front: black card with question */
  .card--front {
    background: var(--card-black);
    color: var(--paper);
    display: flex; flex-direction: column; align-items: center; justify-content: center;
  }
  .claim__dot {
    width: 96px; height: 96px; border-radius: 50%;
    background: var(--paper);
    margin-bottom: 26px;
  }
  .claim { text-align: left; line-height: .95; }
  .claim__strong {
    display: block;
    font-weight: 700; font-size: 62px; letter-spacing: 2px;
  }
  .claim__light {
    display: block;
    font-weight: 300; font-size: 62px; letter-spacing: 1px;
  }

  /* Back: white card with contact details */
  .card--back {
    background: var(--paper);
    color: var(--ink);
    display: flex; flex-direction: column; align-items: center;
    padding-top: 92px;
    text-align: center;
  }
  .brand__dot {
    width: 70px; height: 70px; border-radius: 50%;
    background: var(--ink);
    margin-bottom: 16px;
  }
  .brand {
    font-weight: 700; font-size: 28px; letter-spacing: 1.5px;
    margin-bottom: 16px;
  }
  .tagline {
    font-weight: 400; font-size: 14px; letter-spacing: .6px;
    line-height: 1.4; text-transform: uppercase;
  }
  .rule {
    width: 250px; height: 2px; background: var(--ink);
    margin: 14px 0 14px;
  }
  .person {
    font-weight: 700; font-size: 21px; letter-spacing: .8px;
    text-transform: uppercase;
    margin-bottom: 40px;
  }
  .contact, .social {
    list-style: none;
    font-weight: 400; font-size: 15px; letter-spacing: .6px;
    line-height: 1.4; text-transform: uppercase;
  }
  .social { margin-top: 24px; }
  .social li { display: flex; align-items: center; justify-content: center; gap: 8px; }
  .social__mark { width: 10px; height: 10px; background: var(--ink); flex: none; }
</style>
</head>
<body>
  <main class="stage">
    <section class="card card--front" aria-label="Vorderseite">
      <div class="claim__dot"></div>
      <p class="claim">
        <span class="claim__strong">ANKER</span>
        <span class="claim__light">gefällig?</span>
      </p>
    </section>

    <section class="card card--back" aria-label="Rückseite">
      <div class="brand__dot"></div>
      <p class="brand">PRAXIS ANKERPLATZ</p>
      <p class="tagline">Systemisches Elterncoaching<br>Einzel-, Paar- und Familientherapie</p>
      <div class="rule"></div>
      <p class="person">Miriam Brendel, M.A.</p>
      <ul class="contact">
        <li>www.praxis-ankerplatz.de</li>
        <li>miriam@praxis-ankerplatz.de</li>
        <li>+49 151 8642 0193</li>
      </ul>
      <ul class="social">
        <li><span class="social__mark"></span>praxisankerplatz</li>
        <li><span class="social__mark"></span>praxisankerplatz</li>
      </ul>
    </section>
  </main>
</body>
</html>
```